We have developed a fully functional App called Corvalink. However, it requires a nicer GUI. You can see screenshots of our App on www.corvalink-example.com under "Tutorial". For those of you with Android, you can also install it. When you go to Corvalink-example.com, your phone will automatically redirect you to download. From there, you'll get a better idea of what our App looks like and how your design can make it way better. Please note we expect a design idea for most screens (there's about 8 screens) but do just one screen first and if you win, you can do the other 8 after.

Target Market(s)

People looking for dating / flirting

Industry/Entity Type

Android

Requirements
Must have
• sleek looking

```html
<!DOCTYPE html>
<html lang="en">
<head>
<meta charset="utf-8">
<title>Corvalink – Main Screen</title>
<link rel="stylesheet" href="https://fonts.googleapis.com/css2?family=Roboto:wght@100;300;400;500&display=swap">
<style>
  :root {
    --page-bg: #d3e5e3;
    --status-bar: #111111;
    --teal-light: #4fd3bf;
    --teal-dark: #1bbda5;
    --tab-bg: #eeeeee;
    --tab-icon: #8a8a8a;
    --row-bg: #ffffff;
    --divider: #e4e4e4;
    --avatar: #8c8c8c;
    --avatar-ring: #6f6f6f;
    --name: #1c1c1c;
    --quote: #555555;
    --meta: #9a9a9a;
    --online: #2cc2ac;
    --offline: #e8454a;
    --away: #f5921e;
    --caption: #1a1a1a;
  }
  * { box-sizing: border-box; margin: 0; padding: 0; }
  html, body { width: 882px; height: 1200px; overflow: hidden; }
  body {
    background: var(--page-bg);
    font-family: "Roboto", Arial, sans-serif;
    position: relative;
  }
  .app-screen {
    position: absolute;
    left: 156px; top: 70px;
    width: 570px; height: 940px;
    overflow: hidden;
    background: var(--row-bg);
    box-shadow: 0 6px 24px rgba(0,0,0,.12);
  }
  .status-bar {
    height: 45px; background: var(--status-bar);
    color: #fff; display: flex; align-items: center; justify-content: flex-end;
    gap: 8px; padding-right: 16px; font-size: 24px;
  }
  .app-bar {
    height: 74px;
    background: linear-gradient(90deg, var(--teal-light), var(--teal-dark));
    display: flex; align-items: center; padding: 0 22px; color: #fff;
  }
  .app-bar__title { font-size: 27px; font-weight: 400; flex: 1; }
  .app-bar__actions { display: flex; gap: 26px; }
  .tab-bar {
    height: 74px; background: var(--tab-bg); display: flex; position: relative;
    border-bottom: 1px solid #d8d8d8;
  }
  .tab { flex: 1; display: flex; align-items: center; justify-content: center; }
  .tab--active::after {
    content: ""; position: absolute; left: 0; bottom: -1px;
    width: 190px; height: 5px; background: var(--teal-light);
  }
  .member-row {
    height: 160px; border-bottom: 1px solid var(--divider);
    display: flex; align-items: flex-start; position: relative;
  }
  .member-avatar {
    position: absolute; left: 29px; top: 30px;
    width: 74px; height: 74px; border-radius: 50%;
    background: var(--avatar); border: 2px solid var(--avatar-ring);
  }
  .presence {
    position: absolute; left: 29px; top: 108px; width: 74px; height: 19px;
    border-radius: 4px; color: #fff; font-size: 14px; font-weight: 500;
    text-align: center; line-height: 19px; letter-spacing: .5px;
  }
  .presence--online { background: var(--online); }
  .presence--offline { background: var(--offline); }
  .presence--away { background: var(--away); }
  .member-info { position: absolute; left: 134px; top: 24px; }
  .member-name { font-size: 27px; color: var(--name); font-weight: 400; }
  .member-quote { font-size: 18px; color: var(--quote); font-weight: 300; margin-top: 4px; }
  .member-location {
    position: absolute; left: 134px; top: 117px;
    font-size: 14px; color: var(--meta); display: flex; align-items: center; gap: 6px;
  }
  .row-chevron { position: absolute; right: 38px; top: 66px; }
  .screen-caption {
    position: absolute; left: 0; right: 0; top: 1055px;
    text-align: center; font-size: 84px; font-weight: 100; color: var(--caption);
  }
</style>
</head>
<body>
  <main class="app-screen">
    <div class="status-bar">
      <svg width="28" height="22" viewBox="0 0 28 22"><path d="M14 21 L1 7 Q14 -4 27 7 Z" fill="#fff"/></svg>
      <svg width="20" height="22" viewBox="0 0 20 22"><path d="M19 1 V21 H1 Z" fill="#fff"/></svg>
      <svg width="14" height="24" viewBox="0 0 14 24"><rect x="4" y="0" width="6" height="3" fill="#fff"/><rect x="0" y="3" width="14" height="21" rx="1" fill="#fff"/></svg>
      <span>12:06</span>
    </div>

    <header class="app-bar">
      <h1 class="app-bar__title">Home</h1>
      <div class="app-bar__actions">
        <svg width="36" height="36" viewBox="0 0 36 36" aria-label="Search"><circle cx="14" cy="14" r="10" fill="none" stroke="#fff" stroke-width="3"/><path d="M21 21 L32 32" stroke="#fff" stroke-width="4" stroke-linecap="round"/></svg>
        <svg width="36" height="36" viewBox="0 0 36 36" aria-label="Profile"><circle cx="18" cy="18" r="16" fill="none" stroke="#fff" stroke-width="2.5"/><circle cx="18" cy="14" r="6" fill="#fff"/><path d="M8 29 Q18 16 28 29 Z" fill="#fff"/></svg>
      </div>
    </header>

    <nav class="tab-bar">
      <div class="tab tab--active">
        <svg width="32" height="30" viewBox="0 0 32 30" aria-label="Home"><path d="M16 2 L30 15 H26 V28 H19 V20 H13 V28 H6 V15 H2 Z" fill="var(--teal-light)"/></svg>
      </div>
      <div class="tab">
        <svg width="34" height="30" viewBox="0 0 34 30" aria-label="Messages"><path d="M2 2 H22 V16 H9 L4 21 V16 H2 Z" fill="var(--tab-icon)"/><path d="M12 10 H32 V24 H30 V29 L25 24 H12 Z" fill="var(--tab-icon)" stroke="var(--tab-bg)" stroke-width="2"/></svg>
      </div>
      <div class="tab">
        <svg width="32" height="32" viewBox="0 0 32 32" aria-label="Settings"><g fill="var(--tab-icon)"><circle cx="16" cy="16" r="10"/><rect x="13" y="1" width="6" height="30" rx="1"/><rect x="13" y="1" width="6" height="30" rx="1" transform="rotate(45 16 16)"/><rect x="13" y="1" width="6" height="30" rx="1" transform="rotate(90 16 16)"/><rect x="13" y="1" width="6" height="30" rx="1" transform="rotate(135 16 16)"/></g><circle cx="16" cy="16" r="4.5" fill="var(--tab-bg)"/></svg>
      </div>
    </nav>

    <section class="member-list">
      <article class="member-row">
        <div class="member-avatar" role="img" aria-label="Profile photo of SweetGuy85"></div>
        <span class="presence presence--online">ONLINE</span>
        <div class="member-info">
          <h2 class="member-name">SweetGuy85, 29</h2>
          <p class="member-quote">“Sweet, never sour!”</p>
        </div>
        <p class="member-location"><svg width="10" height="14" viewBox="0 0 10 14"><path d="M5 14 L1 7 A4.5 4.5 0 1 1 9 7 Z" fill="#c8c8c8"/></svg>Los Angeles, USA</p>
        <svg class="row-chevron" width="16" height="26" viewBox="0 0 16 26"><path d="M2 2 L13 13 L2 24" fill="none" stroke="#666" stroke-width="2"/></svg>
      </article>

      <article class="member-row">
        <div class="member-avatar" role="img" aria-label="Profile photo of LookinAround"></div>
        <span class="presence presence--offline">OFFLINE</span>
        <div class="member-info">
          <h2 class="member-name">LookinAround, 24</h2>
          <p class="member-quote">“Goddess &amp; Temptress lives here”</p>
        </div>
        <p class="member-location"><svg width="10" height="14" viewBox="0 0 10 14"><path d="M5 14 L1 7 A4.5 4.5 0 1 1 9 7 Z" fill="#c8c8c8"/></svg>Sacramento, USA</p>
        <svg class="row-chevron" width="16" height="26" viewBox="0 0 16 26"><path d="M2 2 L13 13 L2 24" fill="none" stroke="#666" stroke-width="2"/></svg>
      </article>

      <article class="member-row">
        <div class="member-avatar" role="img" aria-label="Profile photo of MrLonely"></div>
        <span class="presence presence--online">ONLINE</span>
        <div class="member-info">
          <h2 class="member-name">MrLonely, 32</h2>
          <p class="member-quote">“Looking forhappiness &amp; pleasure”</p>
        </div>
        <p class="member-location"><svg width="10" height="14" viewBox="0 0 10 14"><path d="M5 14 L1 7 A4.5 4.5 0 1 1 9 7 Z" fill="#c8c8c8"/></svg>Chicago, USA</p>
        <svg class="row-chevron" width="16" height="26" viewBox="0 0 16 26"><path d="M2 2 L13 13 L2 24" fill="none" stroke="#666" stroke-width="2"/></svg>
      </article>

      <article class="member-row">
        <div class="member-avatar" role="img" aria-label="Profile photo of JaneSants"></div>
        <span class="presence presence--away">AWAY</span>
        <div class="member-info">
          <h2 class="member-name">JaneSants, 28</h2>
          <p class="member-quote">“Smart, Kind &amp; Drama Free!”</p>
        </div>
        <p class="member-location"><svg width="10" height="14" viewBox="0 0 10 14"><path d="M5 14 L1 7 A4.5 4.5 0 1 1 9 7 Z" fill="#c8c8c8"/></svg>Los Angeles, USA</p>
        <svg class="row-chevron" width="16" height="26" viewBox="0 0 16 26"><path d="M2 2 L13 13 L2 24" fill="none" stroke="#666" stroke-width="2"/></svg>
      </article>

      <article class="member-row">
        <div class="member-avatar" role="img" aria-label="Profile photo of SweetGuy85"></div>
        <span class="presence presence--online">ONLINE</span>
        <div class="member-info">
          <h2 class="member-name">SweetGuy85, 29</h2>
          <p class="member-quote">“Sweet, never sour!”</p>
        </div>
        <svg class="row-chevron" width="16" height="26" viewBox="0 0 16 26"><path d="M2 2 L13 13 L2 24" fill="none" stroke="#666" stroke-width="2"/></svg>
      </article>
    </section>
  </main>

  <p class="screen-caption">Main Screen</p>
</body>
</html>
```